BrovaLT BIZ Card, email signature & Stationary

Professional business cards, email signatures and ms word letterhead

Target Market(s)

business owners

Industry/Entity Type

cloud hosting

Contact Information for Business Card

name title office phone number , direct line, fax email address web site

Font styles to use
Other font styles liked:
• something that compliments font in logo

```html
<!DOCTYPE html>
<html lang="en">
<head>
<meta charset="utf-8">
<title>BrovaLT Business Card</title>
<link rel="stylesheet" href="https://fonts.googleapis.com/css2?family=Nunito:wght@400;600;800&display=swap">
<style>
  :root {
    --stage: #6b6b6b;
    --card-dark: #121214;
    --card-light: #fbfbfb;
    --brand-red: #e0231b;
    --ink: #161616;
  }
  html, body {
    margin: 0;
    width: 1200px;
    height: 800px;
    overflow: hidden;
    background: var(--stage);
    font-family: "Nunito", sans-serif;
  }
  .stage {
    position: relative;
    width: 1200px;
    height: 800px;
  }
  .card {
    position: absolute;
    top: 252px;
    width: 520px;
    height: 296px;
    box-sizing: border-box;
    border-bottom: 3px solid var(--brand-red);
    box-shadow: 0 14px 30px rgba(0,0,0,0.35);
  }
  .card-front {
    left: 55px;
    background: var(--card-dark);
    display: flex;
    align-items: center;
    justify-content: center;
  }
  .front-wordmark {
    color: var(--brand-red);
    font-weight: 400;
    font-size: 84px;
    letter-spacing: 1px;
  }
  .card-back {
    left: 625px;
    background: var(--card-light);
    color: var(--ink);
  }
  .back-wordmark {
    position: absolute;
    left: 34px;
    top: 118px;
    font-weight: 800;
    font-size: 34px;
    color: var(--ink);
  }
  .person {
    position: absolute;
    right: 34px;
    top: 34px;
    text-align: left;
  }
  .person-name {
    font-size: 22px;
    font-weight: 800;
    margin: 0;
  }
  .person-name .first { color: var(--brand-red); font-weight: 400; }
  .person-title {
    font-size: 13px;
    margin: 2px 0 0 4px;
  }
  .contact-list {
    position: absolute;
    right: 34px;
    top: 150px;
    list-style: none;
    margin: 0;
    padding: 0;
    font-size: 14px;
  }
  .contact-list li {
    display: flex;
    align-items: center;
    gap: 9px;
    margin-bottom: 6px;
  }
  .contact-list svg { width: 14px; height: 14px; fill: var(--brand-red); }
  .address {
    position: absolute;
    left: 34px;
    bottom: 30px;
    font-size: 14px;
    line-height: 1.35;
    margin: 0;
  }
</style>
</head>
<body>
<main class="stage">
  <section class="card card-front">
    <span class="front-wordmark">BrovaLT</span>
  </section>

  <section class="card card-back">
    <span class="back-wordmark">BrovaLT</span>

    <div class="person">
      <p class="person-name"><span class="first">Dana</span> Whitcombe</p>
      <p class="person-title">President</p>
    </div>

    <ul class="contact-list">
      <li>
        <svg viewBox="0 0 24 24" aria-hidden="true"><path d="M6.6 10.8a15.1 15.1 0 0 0 6.6 6.6l2.2-2.2a1 1 0 0 1 1-.25 11.4 11.4 0 0 0 3.6.57 1 1 0 0 1 1 1V20a1 1 0 0 1-1 1A17 17 0 0 1 3 4a1 1 0 0 1 1-1h3.5a1 1 0 0 1 1 1c0 1.25.2 2.45.57 3.6a1 1 0 0 1-.25 1z"/></svg>
        (888) 555-0142
      </li>
      <li>
        <svg viewBox="0 0 24 24" aria-hidden="true"><path d="M2 5h20v14H2z M2 5l10 8 10-8" /></svg>
        info@brovalt.com
      </li>
      <li>
        <svg viewBox="0 0 24 24" aria-hidden="true"><circle cx="12" cy="12" r="10"/><path d="M2 12h20M12 2v20" stroke="#fbfbfb" stroke-width="1.6" fill="none"/></svg>
        www.brovalt.com
      </li>
    </ul>

    <p class="address">48 Harbor Lane, Suite 210,<br>Austin, TX 78701</p>
  </section>
</main>
</body>
</html>
```